Pebble

My company name is pebble. The logo is attached. I am the business owner.
Name Gideon Thorpe
Phone number- 5553018826
email- Gideon_thorpe@quillnet.net
Website is not live yet but it will be workwithpebble.com
the current beta link is- https://site.brvhosting.com/pebble-v3/
on the back write “ find creative pros”
Use that beta link as reference for typography and colors on card.

```html
<!DOCTYPE html>
<html lang="en">
<head>
<meta charset="UTF-8">
<title>Pebble – Business Card</title>
<link href="https://fonts.googleapis.com/css2?family=Arimo:wght@400;700&display=swap" rel="stylesheet">
<style>
  :root {
    --backdrop: #4a4a4a;
    --card: #2e2e2e;
    --ink: #e2e2e2;
    --ink-soft: #d4d4d4;
    --emboss: #282828;
  }
  * { margin: 0; padding: 0; box-sizing: border-box; }
  html, body { width: 1200px; height: 963px; overflow: hidden; }
  body {
    position: relative;
    background: var(--backdrop);
    font-family: "Arimo", Arial, sans-serif;
    color: var(--ink);
  }
  .card {
    position: absolute;
    top: 174px;
    width: 319px;
    height: 557px;
    background: var(--card);
    text-align: center;
  }
  .card--front { left: 221px; }
  .card--back { left: 636px; }

  .brand-name {
    position: absolute;
    left: 0; right: 0;
    font-weight: 700;
    font-size: 54px;
    letter-spacing: 1px;
    line-height: 1;
    color: var(--ink);
  }
  .card--front .brand-name { top: 99px; }
  .card--back .brand-name { top: 211px; }

  .tagline {
    position: absolute;
    left: 0; right: 0;
    top: 272px;
    font-size: 19px;
    font-weight: 400;
    letter-spacing: 0.3px;
    color: #f0f0f0;
  }
  .brand-name--faint {
    top: 462px !important;
    color: var(--emboss);
  }

  .holder-name {
    position: absolute;
    left: 0; right: 0;
    top: 315px;
    font-size: 24px;
    font-weight: 700;
    letter-spacing: 0.3px;
    color: var(--ink);
  }
  .contact-divider {
    position: absolute;
    left: 74px;
    top: 358px;
  }
  .contact-list {
    position: absolute;
    left: 0; right: 0;
    top: 393px;
    list-style: none;
    font-size: 17px;
    line-height: 22.7px;
    color: var(--ink-soft);
  }
</style>
</head>
<body>

<section class="card card--front">
  <div class="brand-name">PEBBLE</div>
  <h1 class="holder-name">GIDEON THORPE</h1>

  <svg class="contact-divider" width="172" height="20" viewBox="0 0 172 20" aria-hidden="true">
    <line x1="0" y1="10" x2="38" y2="10" stroke="#d4d4d4" stroke-width="1"/>
    <line x1="134" y1="10" x2="172" y2="10" stroke="#d4d4d4" stroke-width="1"/>
    <!-- phone -->
    <circle cx="52" cy="10" r="9" fill="#d9d9d9"/>
    <path d="M48.5 6.2 l1.6-.6 1.2 2.3-1 .9 c.5 1.2 1.3 2 2.5 2.5 l.9-1 2.3 1.2-.6 1.6 c-3.6.2-7.1-3.3-6.9-6.9z" fill="#2e2e2e"/>
    <!-- mail -->
    <circle cx="75" cy="10" r="9" fill="#d9d9d9"/>
    <rect x="70.5" y="6.8" width="9" height="6.4" fill="none" stroke="#2e2e2e" stroke-width="1.1"/>
    <path d="M70.5 6.8 l4.5 3.6 4.5-3.6" fill="none" stroke="#2e2e2e" stroke-width="1.1"/>
    <!-- web -->
    <circle cx="98" cy="10" r="9" fill="#d9d9d9"/>
    <circle cx="98" cy="10" r="4.6" fill="none" stroke="#2e2e2e" stroke-width="1.1"/>
    <path d="M93.4 10 h9.2 M98 5.4 c-2 2.6-2 6.6 0 9.2 M98 5.4 c2 2.6 2 6.6 0 9.2" fill="none" stroke="#2e2e2e" stroke-width="1"/>
    <!-- beta link -->
    <circle cx="120" cy="10" r="9" fill="#d9d9d9"/>
    <circle cx="120" cy="10" r="4.6" fill="none" stroke="#2e2e2e" stroke-width="1.1"/>
    <path d="M115.4 10 h9.2 M120 5.4 c-2 2.6-2 6.6 0 9.2 M120 5.4 c2 2.6 2 6.6 0 9.2" fill="none" stroke="#2e2e2e" stroke-width="1"/>
  </svg>

  <ul class="contact-list">
    <li>5553018826</li>
    <li>Gideon_thorpe@quillnet.net</li>
    <li>workwithpebble.com</li>
    <li>site.brvhosting.com/pebble-v3/</li>
  </ul>
</section>

<section class="card card--back">
  <div class="brand-name">PEBBLE</div>
  <p class="tagline">FIND CREATIVE PROS</p>
  <div class="brand-name brand-name--faint" aria-hidden="true">PEBBLE</div>
</section>

</body>
</html>
```